Halvern Ridge Plants and Nursery needs a business street sign.

I have three businesses located at the same address: The Halvern Ridge Plants & Nursery, The Marrow Stall, and The Brackett Commons. I am looking for a 4’ x 8’ street sign to represent all three businesses as one retail experience. It needs to be eye catching yet simple enough that people can fully read it while driving by. I have logos for the greenhouse and village however I do not have anything for The Marrow Stall. I’m looking for some type of font that’s similar or in between the two attached logos for The Marrow Stall.

Requirements
Must have
• Horizontal Sign, Eye catching, yet simple design so people see it while driving by.
Nice to have
• Horizontal Sign
Should not have
• I’m open to the design being both vertical and horizontal. Please provide both options

```html
<!DOCTYPE html>
<html lang="en">
<head>
<meta charset="utf-8">
<title>Halvern Ridge Plants and Nursery – Street Sign</title>
<link rel="stylesheet" href="https://fonts.googleapis.com/css2?family=Grand+Hotel&display=swap">
<style>
  :root {
    --backdrop: #e6e6e6;
    --cream: #f8f7f2;
    --frame-orange: #e8702a;
    --olive: #5a7a2e;
    --coral: #e84a5a;
    --forest: #2f6b4f;
    --amber: #f08a24;
    --magenta: #e6338f;
    --leaf: #5fa83a;
    --maroon: #8a2b2b;
    --brand-green: #1f7a3a;
    --script: "Grand Hotel", cursive;
  }
  html, body {
    margin: 0;
    width: 1200px;
    height: 1200px;
    overflow: hidden;
    background: var(--backdrop);
  }
  .sign {
    position: absolute;
    left: 320px;
    top: 40px;
    width: 560px;
    height: 1120px;
    overflow: hidden;
  }
  .floral-border {
    position: absolute;
    inset: 0;
    background:
      radial-gradient(circle at 10% 8%, #ef6a4f 0, transparent 14%),
      radial-gradient(circle at 92% 22%, #2f6b5a 0, transparent 16%),
      radial-gradient(circle at 6% 55%, #e8435a 0, transparent 12%),
      radial-gradient(circle at 94% 60%, #f5c27a 0, transparent 13%),
      radial-gradient(circle at 8% 88%, #e0508a 0, transparent 12%),
      radial-gradient(circle at 90% 92%, #3f7a5a 0, transparent 14%),
      linear-gradient(160deg, #7cb45a, #f3a070 45%, #4f8a62 80%, #f0b090);
  }
  .panel {
    position: absolute;
    left: 52px;
    right: 52px;
    top: 38px;
    bottom: 38px;
    background: var(--cream);
    border-radius: 30px;
  }
  .frame {
    position: absolute;
    left: 90px;
    top: 48px;
    width: 382px;
    height: 1025px;
    border: 3px solid var(--frame-orange);
    border-radius: 22px;
    box-sizing: border-box;
  }
  .line {
    position: absolute;
    left: 0;
    width: 100%;
    margin: 0;
    text-align: center;
    font-family: var(--script);
    font-weight: 400;
    line-height: 1;
    white-space: nowrap;
  }
  .title-the { top: 95px; font-size: 62px; color: var(--olive); }
  .title-name { top: 160px; font-size: 74px; color: var(--coral); }
  .rule {
    position: absolute;
    left: 130px;
    top: 278px;
    width: 321px;
    height: 4px;
  }
  .sub-plants { top: 308px; font-size: 50px; color: var(--forest); }
  .sub-plants .joiner { color: var(--amber); font-size: 42px; }
  .sub-nursery { top: 349px; font-size: 82px; color: var(--forest); }
  .flowers { top: 471px; font-size: 44px; color: var(--magenta); }
  .supplies-top { top: 543px; font-size: 57px; color: var(--olive); }
  .supplies-main { top: 595px; font-size: 82px; color: var(--leaf); }
  .shrubbery { top: 711px; font-size: 64px; color: var(--frame-orange); }
  .stall { top: 815px; font-size: 40px; color: var(--maroon); }
  .nursery-name { top: 900px; font-size: 38px; color: var(--brand-green); }
  .commons { top: 993px; font-size: 38px; color: var(--maroon); }
</style>
</head>
<body>
  <main class="sign">
    <div class="floral-border" role="img" aria-label="Watercolour border of tropical flowers, hibiscus, frangipani and green leaves"></div>
    <div class="panel"></div>
    <div class="frame"></div>

    <h1 class="line title-the">The</h1>
    <p class="line title-name">Halvern Ridge</p>
    <svg class="rule" viewBox="0 0 321 4" preserveAspectRatio="none" aria-hidden="true">
      <path d="M0 2 Q160 0 321 2 Q160 4 0 2Z" fill="var(--coral)"/>
    </svg>

    <p class="line sub-plants">Plants <span class="joiner">and</span></p>
    <p class="line sub-nursery">Nursery</p>
    <p class="line flowers">Flowers &amp; Perennials</p>
    <p class="line supplies-top">Garden</p>
    <p class="line supplies-main">Supplies</p>
    <p class="line shrubbery">Shrubbery</p>

    <p class="line stall">Marrow Stall</p>
    <p class="line nursery-name">The Halvern Ridge</p>
    <p class="line commons">Brackett Commons</p>
  </main>
</body>
</html>
```